Willowmere Cremations Business Cards

To create a business card for my company Willowmere Cremations. Remember it is a cremation company.
We want to make sure people have a business card and information. Something modern, professional
100% Online
Prices starting at $695 all-inclusive (prices subject to change without notice).
A business card is the first point of contact with the prospective client.

Contact Information for Business Card

(305) 472-8163
www.WillowmereCremationsMiami.example
willowmerecremations@mailbox.example

Requirements
Must have
• 100% Online
Prices starting at $695 all-inclusive (prices subject to change without notice)

(305) 472-8163

Must match logo style
Should not have
• No black backgrounds. Please only use the white, orange and blue from the logo

```html
<!DOCTYPE html>
<html lang="en">
<head>
<meta charset="utf-8">
<title>Willowmere Cremations – Business Card</title>
<link rel="stylesheet" href="https://fonts.googleapis.com/css2?family=Montserrat:wght@600&family=Poppins:ital,wght@0,400;0,600;1,500;1,800&display=swap">
<style>
  :root {
    --page-bg: #e6e3de;
    --card-bg-top: #f7f8f9;
    --card-bg-bottom: #e9edf0;
    --brand-orange: #e0521f;
    --brand-blue: #1f7fc4;
    --tagline-blue: #1565b5;
    --text-light: #fdf1ea;
  }
  * { box-sizing: border-box; margin: 0; padding: 0; }
  html, body { width: 1200px; height: 970px; overflow: hidden; }
  body { background: var(--page-bg); position: relative; font-family: "Poppins", sans-serif; }

  .business-card {
    position: absolute; left: 80px; top: 188px;
    width: 1040px; height: 594px;
    border-radius: 22px; overflow: hidden;
    background: linear-gradient(170deg, var(--card-bg-top), var(--card-bg-bottom));
    box-shadow: 0 18px 40px rgba(0,0,0,0.18);
  }
  .card-shapes { position: absolute; inset: 0; width: 100%; height: 100%; }

  .brand-name {
    position: absolute; left: 30px; top: 250px; width: 442px;
    text-align: center; color: var(--brand-blue);
    font-family: "Montserrat", sans-serif; font-weight: 600;
    line-height: 1;
  }
  .brand-name .brand-primary { display: block; font-size: 46px; letter-spacing: 3px; }
  .brand-name .brand-secondary { display: block; font-size: 22px; letter-spacing: 7px; margin-top: 14px; }

  .offer { position: absolute; right: 48px; top: 72px; text-align: right; }
  .offer-headline { font-size: 34px; font-weight: 800; font-style: italic; color: var(--tagline-blue); line-height: 1.1; }
  .offer-price { font-size: 22px; font-weight: 500; font-style: italic; color: var(--brand-orange); margin-top: 6px; }

  .contact-person { position: absolute; right: 46px; top: 335px; text-align: right; color: var(--text-light); }
  .person-name { font-size: 32px; font-weight: 600; line-height: 1.1; letter-spacing: 0.5px; }
  .person-role { font-size: 23px; font-weight: 400; margin-top: 2px; }

  .contact-list { position: absolute; right: 48px; top: 428px; list-style: none; }
  .contact-item {
    display: flex; justify-content: flex-end; align-items: center;
    height: 40px; gap: 16px;
    font-size: 23px; color: var(--text-light);
  }
  .contact-icon { width: 30px; height: 30px; flex: none; }
</style>
</head>
<body>
  <article class="business-card">
    <svg class="card-shapes" viewBox="0 0 1180 675" preserveAspectRatio="none" aria-hidden="true">
      <defs>
        <linearGradient id="waveOrange" x1="0" y1="1" x2="1" y2="0">
          <stop offset="0" stop-color="#ef7a2c"/>
          <stop offset="0.5" stop-color="#d9481a"/>
          <stop offset="1" stop-color="#d84316"/>
        </linearGradient>
      </defs>
      <path class="wave-orange" fill="url(#waveOrange)"
            d="M0 610 C170 650 380 610 540 480 C720 330 870 255 1180 265 L1180 675 L0 675 Z"/>
      <path class="wave-white" fill="#f4f1ee"
            d="M0 560 C150 600 360 585 585 400 C380 600 160 630 0 600 Z"/>
      <path class="wave-blue" fill="#1f7fc4"
            d="M0 490 C130 560 320 590 590 395 C340 575 140 590 0 548 Z"/>
    </svg>

    <h1 class="brand-name">
      <span class="brand-primary">WILLOWMERE</span>
      <span class="brand-secondary">CREMATIONS</span>
    </h1>

    <div class="offer">
      <p class="offer-headline">100% Online</p>
      <p class="offer-price">Starting at $695 all-inclusive</p>
    </div>

    <div class="contact-person">
      <p class="person-name">DANIEL REYES</p>
      <p class="person-role">Manager</p>
    </div>

    <ul class="contact-list">
      <li class="contact-item">
        <span>(305) 472-8163</span>
        <svg class="contact-icon" viewBox="0 0 30 30" aria-label="Phone">
          <circle cx="15" cy="15" r="13" fill="none" stroke="#fdf1ea" stroke-width="2"/>
          <rect x="10.5" y="7.5" width="9" height="15" rx="1.8" fill="none" stroke="#fdf1ea" stroke-width="1.8"/>
          <line x1="13.5" y1="19.5" x2="16.5" y2="19.5" stroke="#fdf1ea" stroke-width="1.6"/>
        </svg>
      </li>
      <li class="contact-item">
        <span>willowmerecremations@mailbox.example</span>
        <svg class="contact-icon" viewBox="0 0 30 30" aria-label="Email">
          <circle cx="15" cy="15" r="13" fill="none" stroke="#fdf1ea" stroke-width="2"/>
          <rect x="8" y="10" width="14" height="10" rx="1" fill="#fdf1ea"/>
          <path d="M8.5 10.5 L15 16 L21.5 10.5 M8.5 19.5 L13 15 M21.5 19.5 L17 15" fill="none" stroke="#d9481a" stroke-width="1.3"/>
        </svg>
      </li>
      <li class="contact-item">
        <span>www.WillowmereCremationsMiami.example</span>
        <svg class="contact-icon" viewBox="0 0 30 30" aria-label="Website">
          <circle cx="15" cy="15" r="13" fill="none" stroke="#fdf1ea" stroke-width="2"/>
          <circle cx="15" cy="15" r="8" fill="none" stroke="#fdf1ea" stroke-width="1.5"/>
          <ellipse cx="15" cy="15" rx="3.5" ry="8" fill="none" stroke="#fdf1ea" stroke-width="1.3"/>
          <line x1="7" y1="15" x2="23" y2="15" stroke="#fdf1ea" stroke-width="1.3"/>
        </svg>
      </li>
    </ul>
  </article>
</body>
</html>
```